Logo & Website Reference Design for "PineRidge.Trips"

Hi there!

I like to get a logo, website incl. fonts reference design for "Pine Ridge Trips". The URL will be PineRidge.Trips or Pine-Ridge.Trips and would like to have a memorable symbol, too. Basically, the symbol should not be a OffRoad car rather than e.g. Mountains, Trails, skid-marks etc.. The website and activities I will provide video documented of off-road trails with off-road cars; mainly off-road campers and POI's will be mentioned online. Not "extreme Off-Road" folks with their Brakmor Valiants or Quillet Roamers rather than more mainstream. It would be great if you could consider Halvenau Camper Vans (modern, K3 or K4) that are offroad capable (higher, extreme tires, snorkel etc.).

If you work on the sample images for the website, pls make use of e.g. off-road trails (gravel roads) thru forest, mountains, rocks etc. - no street roads.

Also, I am planning to manage the website content with plimo.example - if you have any experience - much appreciated. Alternatively, I am also happy with e.g. PageKilnly to manage the content in the close future on my onwn.

Target Market(s)

Key target audience are mainly male people in Central- Northern- and Benelux Europe in the age of 28 - 55 years.

Industry/Entity Type

Tourism

Logo Text

Pine-Ridge.Trips or PineRidge.Trips (please recommend with "-" or w/o)

Number of Pages Required

4 page

Font styles to use
Sans Serif

Colors

Designer to choose colors to be used in the design.

Requirements
Must have
• Modern and attractive logo with symbol that works w/o text (PineRidge.Trips).
• Webdesign must work on mobile devices (responsive) as well as on computer browsers
Nice to have
• Even if URL is PineRidge.Trips and/or Pine-Ridge.Trips the sub-slogan could be used e.g. real off-road tours | virtual
• Favicon for website

```html
<!DOCTYPE html>
<html lang="en">
<head>
<meta charset="utf-8">
<title>PineRidge.Trips</title>
<link href="https://fonts.googleapis.com/css2?family=Montserrat:wght@300;400;600;700;800&family=Roboto:wght@400;500&family=Playfair+Display:wght@400&display=swap" rel="stylesheet">
<style>
:root{
  --ink:#1f1f1f;
  --muted:#555;
  --gold:#d9b85a;
  --navy:#13233a;
  --navy-deep:#0c1726;
  --footer-text:#c9d0da;
  --field-line:#6d7b8e;
  --white:#fff;
}
*{margin:0;padding:0;box-sizing:border-box}
html,body{width:1200px;height:2526px;overflow:hidden;background:var(--white)}
body{position:relative;font-family:'Roboto',sans-serif;color:var(--ink)}
.abs{position:absolute}

/* header */
.site-header{position:absolute;left:0;top:0;width:1200px;height:105px;background:var(--white);box-shadow:0 2px 6px rgba(0,0,0,.12);z-index:2}
.brand{position:absolute;left:175px;top:26px;display:flex;align-items:center;gap:12px;font-family:'Montserrat',sans-serif;font-weight:800;font-size:17px;color:var(--navy);letter-spacing:.4px}
.brand-mark{width:50px;height:50px;border-radius:50%;background:var(--navy)}
.account{position:absolute;left:920px;top:18px;font-family:'Montserrat',sans-serif;font-size:11px;color:#333;display:flex;align-items:center;gap:8px}
.main-nav{position:absolute;left:575px;top:62px;display:flex;gap:20px;font-family:'Montserrat',sans-serif;font-size:13px;color:#222}

/* hero */
.hero{left:0;top:105px;width:1200px;height:421px;background:
  radial-gradient(ellipse 260px 150px at 640px 250px,rgba(40,42,48,.75),rgba(40,42,48,0)),
  radial-gradient(ellipse 220px 140px at 900px 360px,rgba(96,92,58,.85),rgba(96,92,58,0)),
  linear-gradient(180deg,#a9bccd 0%,#8ea7bd 14%,#3f6a8e 24%,#6d8fa8 36%,#b9b3a0 44%,#9f9a7c 54%,#6f7b45 70%,#56652f 100%)}
.play-ring{position:absolute;width:68px;height:68px;border:3px solid var(--white);border-radius:50%}
.play-ring svg{position:absolute;left:22px;top:18px}
.hero-title{left:0;top:288px;width:1200px;text-align:center;font-family:'Playfair Display',serif;font-weight:400;font-size:42px;color:var(--white);text-shadow:0 1px 3px rgba(0,0,0,.25)}

/* tours */
.section-title{left:0;top:586px;width:1200px;text-align:center;font-family:'Montserrat',sans-serif;font-weight:700;font-size:24px;letter-spacing:1px}
.section-lead{left:0;top:640px;width:1200px;text-align:center;font-size:18px;color:var(--muted)}
.tour-card{position:absolute;width:281px}
.tour-media{position:relative;width:281px;height:181px}
.tour-play{position:absolute;left:115px;top:65px;width:50px;height:50px;border-radius:50%;background:rgba(19,35,58,.55);border:2px solid var(--white)}
.tour-play svg{position:absolute;left:17px;top:13px}
.tour-title{margin-top:28px;font-family:'Montserrat',sans-serif;font-weight:600;font-size:17px;color:#222}
.tour-text{margin-top:10px;font-size:11px;line-height:21px;color:#555}
.btn-more{left:534px;top:1425px;width:133px;height:43px;background:var(--gold);color:var(--white);font-family:'Montserrat',sans-serif;font-weight:600;font-size:13px;display:flex;align-items:center;justify-content:center}

/* video band */
.video-band{left:0;top:1533px;width:1200px;height:487px;background:
  radial-gradient(ellipse 420px 90px at 600px 470px,rgba(40,48,62,.95),rgba(40,48,62,0)),
  radial-gradient(ellipse 380px 120px at 520px 300px,rgba(196,150,100,.8),rgba(196,150,100,0)),
  linear-gradient(180deg,#9fb6cc 0%,#8ea2a8 6%,#6f6a46 18%,#7d6a44 34%,#a3794c 52%,#8a6540 72%,#5a4a36 86%,#2c3646 100%)}
.video-title{left:0;top:1740px;width:1200px;text-align:center;font-family:'Montserrat',sans-serif;font-weight:400;font-size:44px;line-height:60px;color:var(--white);letter-spacing:1px;text-shadow:0 2px 6px rgba(0,0,0,.3)}

/* footer */
.site-footer{left:0;top:2020px;width:1200px;height:423px;background:var(--navy);color:var(--footer-text)}
.footer-col{position:absolute;top:90px}
.footer-heading{font-family:'Montserrat',sans-serif;font-weight:600;font-size:17px;color:var(--white)}
.footer-rule{width:72px;height:1px;background:var(--footer-text);margin-top:10px}
.contact-line{display:flex;gap:14px;font-size:12px;line-height:20px;margin-top:14px;color:var(--white)}
.contact-line svg{flex:none;margin-top:3px}
.social{display:flex;gap:18px;margin:28px 0 0 36px}
.social span{width:10px;height:10px;border-radius:50%;background:var(--white)}
.field{width:196px;border:1px solid var(--field-line);color:#8b97a8;font-size:11px;padding:7px 10px;margin-top:6px}
.btn-gold{background:var(--gold);color:var(--white);font-family:'Montserrat',sans-serif;font-weight:600;font-size:12px;display:flex;align-items:center;justify-content:center}
.blog-list{list-style:none;margin-top:10px}
.blog-list li{font-size:12px;line-height:22.6px;color:var(--white);display:flex;align-items:center;gap:14px}
.blog-list li::before{content:"";width:6px;height:6px;border-radius:50%;background:var(--white)}
.news-text{width:175px;font-size:12px;line-height:20px;margin:14px 0 0 -6px;color:var(--white)}
.footer-bottom{left:0;top:2443px;width:1200px;height:83px;background:var(--navy-deep);color:#9aa5b4;font-size:11px}
.copyright{position:absolute;left:182px;top:32px}
.to-top{position:absolute;left:1027px;top:23px;width:34px;height:34px;background:var(--gold);display:flex;align-items:center;justify-content:center}
</style>
</head>
<body>

<header class="site-header">
  <div class="brand"><span class="brand-mark"></span>PINERIDGE.TRIPS</div>
  <div class="account">
    <svg width="10" height="11" viewBox="0 0 10 11"><circle cx="5" cy="3" r="2.6" fill="#222"/><path d="M0 11c0-3.5 2.2-5 5-5s5 1.5 5 5z" fill="#222"/></svg>
    Login/Register
  </div>
  <nav class="main-nav"><span>Home</span><span>About Us</span><span>Trip Styles</span><span>Destination</span><span>Videos</span><span>Contact Us</span></nav>
</header>

<section class="abs hero" role="img" aria-label="Campers setting up a tent beside an off-road car with an awning at the beach"></section>
<div class="play-ring" style="left:566px;top:214px"><svg width="26" height="30" viewBox="0 0 26 30"><path d="M2 2l22 13L2 28z" fill="none" stroke="#fff" stroke-width="3"/></svg></div>
<h1 class="abs hero-title">Virtual Pine Ridge Trips</h1>

<h2 class="abs section-title">POPULAR TOURS</h2>
<p class="abs section-lead">Excepteur sint occaecat cupidatat non proident sunt in culpa qui officia</p>

<article class="tour-card" style="left:162px;top:730px">
  <div class="tour-media" role="img" aria-label="Off-road car parked by a mountain lake with campers" style="background:linear-gradient(180deg,#b9cde2 0%,#8fb0d2 28%,#9aa6b0 40%,#5f7a98 52%,#7d8472 68%,#5e6b44 100%)"><div class="tour-play"><svg width="18" height="22" viewBox="0 0 18 22"><path d="M2 2l14 9L2 20z" fill="#fff"/></svg></div></div>
  <h3 class="tour-title">Nemo enim ipsam voluptatem</h3>
  <p class="tour-text">Nam libero tempore, cum soluta nobis est eligendi optio cumque nihil impedit quo minus id quod maxime placeat facere possimus omnis</p>
</article>
<article class="tour-card" style="left:457px;top:730px">
  <div class="tour-media" role="img" aria-label="White off-road car and tent on a grassy meadow" style="background:radial-gradient(ellipse 90px 50px at 110px 110px,rgba(225,228,230,.8),rgba(225,228,230,0)),linear-gradient(180deg,#3f7fd0 0%,#7aa7dc 40%,#aac2d8 55%,#6f9140 72%,#557a2e 100%)"><div class="tour-play"><svg width="18" height="22" viewBox="0 0 18 22"><path d="M2 2l14 9L2 20z" fill="#fff"/></svg></div></div>
  <h3 class="tour-title">Nemo enim ipsam voluptatem</h3>
  <p class="tour-text">Nam libero tempore, cum soluta nobis est eligendi optio cumque nihil impedit quo minus id quod maxime placeat facere possimus omnis</p>
</article>
<article class="tour-card" style="left:756px;top:730px">
  <div class="tour-media" role="img" aria-label="Travellers sitting on an off-road car in a dry landscape" style="background:radial-gradient(ellipse 80px 70px at 140px 120px,rgba(50,52,50,.7),rgba(50,52,50,0)),linear-gradient(180deg,#4a8ad6 0%,#8ab2de 45%,#b4b09a 62%,#9a8a62 80%,#7e6e4c 100%)"><div class="tour-play"><svg width="18" height="22" viewBox="0 0 18 22"><path d="M2 2l14 9L2 20z" fill="#fff"/></svg></div></div>
  <h3 class="tour-title">Nemo enim ipsam voluptatem</h3>
  <p class="tour-text">Nam libero tempore, cum soluta nobis est eligendi optio cumque nihil impedit quo minus id quod maxime placeat facere possimus omnis</p>
</article>

<article class="tour-card" style="left:162px;top:1063px">
  <div class="tour-media" role="img" aria-label="Red off-road car crossing a forest creek" style="background:radial-gradient(ellipse 70px 50px at 120px 95px,rgba(170,40,30,.75),rgba(170,40,30,0)),linear-gradient(135deg,#3e4a2c 0%,#5d6640 30%,#7a6e55 55%,#a09478 80%,#8a8470 100%)"><div class="tour-play"><svg width="18" height="22" viewBox="0 0 18 22"><path d="M2 2l14 9L2 20z" fill="#fff"/></svg></div></div>
  <h3 class="tour-title">Nemo enim ipsam voluptatem</h3>
  <p class="tour-text">Nam libero tempore, cum soluta nobis est eligendi optio cumque nihil impedit quo minus id quod maxime placeat facere possimus omnis</p>
</article>
<article class="tour-card" style="left:457px;top:1063px">
  <div class="tour-media" role="img" aria-label="Group standing beside an off-road car on a forest trail" style="background:radial-gradient(ellipse 70px 45px at 150px 130px,rgba(60,40,36,.7),rgba(60,40,36,0)),linear-gradient(180deg,#6a9a44 0%,#4f7a32 35%,#3f6a2c 60%,#7a7a6e 80%,#6c6a5e 100%)"><div class="tour-play"><svg width="18" height="22" viewBox="0 0 18 22"><path d="M2 2l14 9L2 20z" fill="#fff"/></svg></div></div>
  <h3 class="tour-title">Nemo enim ipsam voluptatem</h3>
  <p class="tour-text">Nam libero tempore, cum soluta nobis est eligendi optio cumque nihil impedit quo minus id quod maxime placeat facere possimus omnis</p>
</article>
<article class="tour-card" style="left:756px;top:1063px">
  <div class="tour-media" role="img" aria-label="Convoy of off-road cars on a rocky valley track" style="background:linear-gradient(100deg,#4e6038 0%,#6b7650 30%,rgba(107,118,80,0) 45%),linear-gradient(180deg,#8aa7c6 0%,#6f8260 30%,#8a7a60 55%,#a09c94 78%,#8e8a82 100%)"><div class="tour-play"><svg width="18" height="22" viewBox="0 0 18 22"><path d="M2 2l14 9L2 20z" fill="#fff"/></svg></div></div>
  <h3 class="tour-title">Nemo enim ipsam voluptatem</h3>
  <p class="tour-text">Nam libero tempore, cum soluta nobis est eligendi optio cumque nihil impedit quo minus id quod maxime placeat facere possimus omnis</p>
</article>

<div class="abs btn-more">VIEW MORE</div>

<section class="abs video-band" role="img" aria-label="Driver's view of an off-road car on a dusty hillside trail"></section>
<div class="play-ring" style="left:566px;top:1650px"><svg width="26" height="30" viewBox="0 0 26 30"><path d="M2 2l22 13L2 28z" fill="none" stroke="#fff" stroke-width="3"/></svg></div>
<h2 class="abs video-title">Offroad 360 Video at<br>Cedar Hollow, Marlow Bay</h2>

<footer class="abs site-footer">
  <div class="footer-col" style="left:172px;width:190px">
    <h4 class="footer-heading">Contact Us</h4>
    <div class="footer-rule"></div>
    <div class="contact-line" style="margin-top:24px"><svg width="9" height="13" viewBox="0 0 9 13"><path d="M4.5 0A4.5 4.5 0 0 0 0 4.5C0 8 4.5 13 4.5 13S9 8 9 4.5A4.5 4.5 0 0 0 4.5 0z" fill="#fff"/><circle cx="4.5" cy="4.5" r="1.6" fill="#13233a"/></svg><span>112, voluptates repudiandae sint et molestiae non</span></div>
    <div class="contact-line"><svg width="12" height="12" viewBox="0 0 12 12"><path d="M2.5 0l2 3-1.3 1.3a7 7 0 0 0 4.5 4.5L9 7.5l3 2-1.5 2.5C5 12 0 7 0 1.5z" fill="#fff"/></svg><span>(00) 0000 0000</span></div>
    <div class="contact-line"><svg width="13" height="10" viewBox="0 0 13 10"><rect width="13" height="10" rx="1" fill="#fff"/><path d="M0.5 1l6 4.5 6-4.5" fill="none" stroke="#13233a" stroke-width="1.2"/></svg><span>info@pineridge.trips</span></div>
    <div class="social"><span></span><span></span><span></span><span></span></div>
  </div>
  <div class="footer-col" style="left:391px">
    <h4 class="footer-heading">Quick Contact</h4>
    <div class="footer-rule"></div>
    <div class="field" style="margin-top:28px">Name...</div>
    <div class="field">Email...</div>
    <div class="field" style="height:100px">Message...</div>
    <div class="btn-gold" style="width:196px;height:31px;margin-top:8px">SUBMIT</div>
  </div>
  <div class="footer-col" style="left:610px">
    <h4 class="footer-heading">Recen Blog</h4>
    <div class="footer-rule"></div>
    <ul class="blog-list">
      <li>Nam libero tempore cum soluta</li>
      <li>Est eligendi optio cumque nihil</li>
      <li>Minus id quod maxime placeat</li>
      <li>Mis voluptas assumenda est</li>
      <li>Omnis dolor repellendus</li>
      <li>Temporibus autem quibusdam</li>
    </ul>
  </div>
  <div class="footer-col" style="left:836px;width:200px">
    <h4 class="footer-heading">Newsletter</h4>
    <div class="footer-rule"></div>
    <p class="news-text">Subscribe to our newsletter for latest videos</p>
    <div class="field" style="margin:10px 0 0 -6px">Email...</div>
    <div class="btn-gold" style="width:196px;height:30px;margin:6px 0 0 -6px">SUBSCRIBE</div>
  </div>
</footer>

<div class="abs footer-bottom">
  <span class="copyright">©Copyright Information here</span>
  <div class="to-top"><svg width="12" height="8" viewBox="0 0 12 8"><path d="M1 7l5-5 5 5" fill="none" stroke="#fff" stroke-width="2"/></svg></div>
</div>

</body>
</html>
```